Create branded design templates/backgrounds for social media based on UK property investing company

I'd like Instagram, Facebook and Linkedin backgrounds/templates to add text to, based on my logo design and business of UK holiday let investing. Ideally I'd have some base designs for me to approve, then engage with the winning designer further to create about 50 different templates. I looking for a mixture of templates with the logo and using logo colours, others of internal holiday let photos including logos and a few of my photo imposed on the front of them.
Updates

Slow in providing feedback

Target Market(s)

Middle aged adults

Industry/Entity Type

Holiday let properties

Requirements
Must have
• a distinct brand look that can be replicated

```html
<!DOCTYPE html>
<html lang="en">
<head>
<meta charset="UTF-8">
<title>Harbourly social templates</title>
<link href="https://fonts.googleapis.com/css2?family=Montserrat:wght@500&display=swap" rel="stylesheet">
<style>
  :root {
    --stage: #000000;
    --green: #6cb52d;
    --green-light: #8fcc5a;
    --blue: #1b8fd6;
    --blue-deep: #1f63cf;
    --cyan: #1ec3ec;
    --yellow: #fbd93c;
    --white: #ffffff;
    --ink: #3a3f4a;
  }
  * { margin: 0; padding: 0; box-sizing: border-box; }
  html, body {
    width: 1200px;
    height: 632px;
    overflow: hidden;
    background: var(--stage);
  }
  .stage {
    position: relative;
    width: 1200px;
    height: 632px;
  }
  .template {
    position: absolute;
    top: 70px;
    width: 393px;
    height: 491px;
    overflow: hidden;
  }
  .template--green { left: 173px; }
  .template--blue { left: 634px; }

  .portrait {
    position: absolute;
    inset: 0;
  }
  .template--green .portrait {
    background:
      radial-gradient(ellipse 38% 45% at 48% 38%, rgba(255,255,255,0.18), transparent 70%),
      linear-gradient(120deg, var(--green-light) 0%, var(--green) 70%, #5faa22 100%);
  }
  .template--blue .portrait {
    background:
      radial-gradient(ellipse 38% 45% at 48% 40%, rgba(40,150,230,0.55), transparent 72%),
      linear-gradient(115deg, var(--cyan) 0%, var(--blue) 45%, var(--blue-deep) 100%);
  }

  .waves {
    position: absolute;
    inset: 0;
    width: 100%;
    height: 100%;
  }

  .brand {
    position: absolute;
    left: 0;
    right: 0;
    display: flex;
    align-items: center;
    justify-content: center;
    gap: 10px;
    font-family: 'Montserrat', sans-serif;
    font-weight: 500;
  }
  .brand__mark {
    width: 40px;
    height: 40px;
  }
  .brand__name {
    font-size: 17px;
    line-height: 1.05;
    letter-spacing: 0.5px;
  }
  .brand__name span { display: block; }
  .brand__name .upper { text-transform: uppercase; font-size: 17px; }

  .template--green .brand { top: 203px; color: var(--white); }
  .template--green .brand__mark { background: var(--white); }
  .template--blue .brand { top: 425px; color: var(--ink); }
  .template--blue .brand__mark { background: var(--blue); }
</style>
</head>
<body>
<main class="stage">

  <section class="template template--green">
    <div class="portrait" role="img" aria-label="Green-tinted portrait photo of the company founder"></div>
    <svg class="waves" viewBox="0 0 839 1047" preserveAspectRatio="none">
      <path fill="var(--yellow)" d="M0 708 C130 712 300 740 420 780 C600 835 720 855 839 865 L839 1047 L0 1047 Z"/>
      <path fill="var(--white)" d="M0 790 C150 770 330 780 520 805 C680 830 760 870 839 890 L839 1047 L0 1047 Z"/>
      <path fill="var(--blue)" d="M0 850 C170 820 340 825 530 845 C680 865 770 900 839 925 L839 1047 L0 1047 Z"/>
    </svg>
    <div class="brand">
      <div class="brand__mark"></div>
      <div class="brand__name"><span>Holidays by</span><span class="upper">Harbourly</span></div>
    </div>
  </section>

  <section class="template template--blue">
    <div class="portrait" role="img" aria-label="Blue-tinted portrait photo of the company founder"></div>
    <svg class="waves" viewBox="0 0 839 1047" preserveAspectRatio="none">
      <path fill="var(--yellow)" d="M0 855 C200 840 420 800 600 750 C700 722 780 708 839 702 L839 1047 L0 1047 Z"/>
      <path fill="var(--green)" d="M0 890 C220 860 430 830 600 800 C700 782 780 778 839 780 L839 1047 L0 1047 Z"/>
      <path fill="var(--white)" d="M0 918 C220 885 420 852 600 830 C700 820 790 830 839 845 L839 1047 L0 1047 Z"/>
    </svg>
    <div class="brand">
      <div class="brand__mark"></div>
      <div class="brand__name"><span>Holidays by</span><span class="upper">Harbourly</span></div>
    </div>
  </section>

</main>
</body>
</html>
```